Organic Label

Brindle Cove Pantry grow micro greens and sprouts for the Canadian market. We need a food label for an organic "Alfalfa" sprout. We need to have English and french on the label our logo, the product name, weight, Canadian flag, UPC, keep refrigerated, pre-washed, an organic logo, postal code

Target Market(s)

Health food, Yuppies, Hipsters, Health conscious individuals ranging from 30 to 60 years

Industry/Entity Type

Health And Wellness

Colors
9bcb3c

Requirements
Must have
• We need to have English and french on the label our logo, the product name, weight, Canadian flag, UPC, keep refrigerated, pre-washed, an organic logo, postal code.
Nice to have
• Would like to see a label will a back ground look of a cardboard or rustic cotton. Not sure if that would look good but would love to see it.

```html
<!DOCTYPE html>
<html lang="en">
<head>
<meta charset="utf-8">
<title>Brindle Cove Pantry – Organic Alfalfa Sprouts Labels</title>
<link rel="stylesheet" href="https://fonts.googleapis.com/css2?family=Caveat:wght@500&family=Play:wght@400;700&family=Arimo:wght@400;700&display=swap">
<style>
  :root {
    --page: #ffffff;
    --ink: #1c1c1a;
    --white: #ffffff;
    --organic-green: #3d7c35;
    --red-ribbon: #a52126;
    --purple-ribbon: #a66ca0;
    --purple-light: #c9a2c4;
    --olive: #a9bf3a;
    --olive-light: #c8d46a;
    --badge-green: #3f9a3c;
    --flag-red: #d52b1e;
    --upc-panel: #f4f4f0;
  }
  * { margin: 0; padding: 0; box-sizing: border-box; }
  html, body { width: 1200px; height: 844px; overflow: hidden; background: var(--page); }
  .sheet { position: relative; width: 1200px; height: 844px; }
  .label {
    position: absolute; top: 107px; width: 338px; height: 579px;
    box-shadow: 3px 4px 8px rgba(0,0,0,0.28);
  }
  .label svg { display: block; width: 100%; height: 100%; }
  .label--red { left: 54px; }
  .label--spring { left: 423px; }
  .label--lime { left: 792px; }
  .brand { font-family: "Play", sans-serif; font-size: 33px; fill: var(--ink); }
  .organic { font-family: "Play", sans-serif; font-size: 34px; fill: var(--organic-green); }
  .product { font-family: "Caveat", cursive; font-size: 92px; fill: var(--white); }
  .sprouts { font-family: "Play", sans-serif; font-size: 40px; fill: var(--ink); }
  .french { font-family: "Caveat", cursive; font-size: 44px; fill: var(--white); }
  .arc-text { font-family: "Play", sans-serif; font-size: 16px; fill: var(--ink); }
  .small { font-family: "Arimo", sans-serif; font-size: 10.5px; fill: var(--ink); }
  .tiny { font-family: "Arimo", sans-serif; font-size: 8.5px; font-weight: 700; fill: var(--ink); }
  .weight { font-family: "Arimo", sans-serif; font-size: 19px; font-weight: 700; fill: var(--ink); }
  .postal { font-family: "Arimo", sans-serif; font-size: 10.5px; font-weight: 700; fill: var(--ink); }
  .origin { font-family: "Arimo", sans-serif; font-size: 13.5px; font-weight: 700; fill: var(--ink); }
</style>
</head>
<body>
<main class="sheet">

  <!-- Red ribbon / cream variant -->
  <div class="label label--red">
    <svg viewBox="0 0 405 695" role="img" aria-label="Brindle Cove Pantry organic alfalfa sprouts label, cream and dark green">
      <defs>
        <path id="arcPre1" d="M212,640 Q240,545 395,508"/>
        <path id="arcWeb1" d="M236,650 Q262,590 400,568"/>
      </defs>
      <rect width="405" height="695" fill="#ece9d2"/>
      <path d="M0,337 Q300,350 405,490 L405,695 L0,695 Z" fill="#e4dfc3"/>
      <path d="M0,480 Q220,470 330,695 L0,695 Z" fill="#d9d1b5"/>
      <path d="M0,290 Q180,195 405,197 L405,490 Q300,350 0,337 Z" fill="#4b8b3f"/>
      <path d="M168,695 Q200,520 405,480 L405,695 Z" fill="#ece9d2"/>
      <path d="M168,695 Q200,520 405,480" fill="none" stroke="var(--olive)" stroke-width="11"/>
      <path d="M200,695 Q228,565 405,540" fill="none" stroke="var(--olive)" stroke-width="5"/>
      <path d="M228,695 Q255,598 405,585" fill="none" stroke="var(--olive-light)" stroke-width="5"/>
      <path d="M28,0 H106 V150 L67,132 L28,150 Z" fill="var(--red-ribbon)"/>
      <circle cx="67" cy="82" r="52" fill="var(--white)" stroke="var(--red-ribbon)" stroke-width="3"/>
      <circle cx="67" cy="82" r="30" fill="var(--badge-green)"/>
      <text class="brand" x="392" y="80" text-anchor="end">Brindle Cove</text>
      <text class="brand" x="392" y="118" text-anchor="end">Pantry</text>
      <text class="organic" x="380" y="183" text-anchor="end">organic</text>
      <text class="product" x="382" y="285" text-anchor="end">Alfalfa</text>
      <text class="sprouts" x="382" y="340" text-anchor="end">SPROUTS</text>
      <text class="french" x="382" y="388" text-anchor="end">Luzerne</text>
      <text class="arc-text"><textPath href="#arcPre1" startOffset="40">PRE-WASHED</textPath></text>
      <text class="arc-text"><textPath href="#arcWeb1" startOffset="8">brindlecovepantry.ca</textPath></text>
      <text class="small" x="15" y="592">KEEP REFRIGERATED</text>
      <text class="small" x="15" y="606">GARDER RÉFRIGÉRATÉ</text>
      <rect x="15" y="615" width="162" height="65" fill="var(--upc-panel)"/>
      <text class="weight" x="305" y="640">100g</text>
      <text class="tiny" x="353" y="631">NET WT</text>
      <text class="tiny" x="353" y="641">POIDS NET</text>
      <text class="postal" x="394" y="661" text-anchor="end">B3K 5X7</text>
      <rect x="257" y="668" width="22" height="13" fill="var(--white)" stroke="#ccc" stroke-width="0.5"/>
      <rect x="257" y="668" width="6" height="13" fill="var(--flag-red)"/>
      <rect x="273" y="668" width="6" height="13" fill="var(--flag-red)"/>
      <rect x="266" y="671" width="4" height="7" fill="var(--flag-red)"/>
      <text class="origin" x="394" y="681" text-anchor="end">Grown in Canada</text>
    </svg>
  </div>

  <!-- Purple ribbon / spring green variant -->
  <div class="label label--spring">
    <svg viewBox="0 0 405 695" role="img" aria-label="Brindle Cove Pantry organic alfalfa sprouts label, spring green and purple">
      <defs>
        <path id="arcPre2" d="M212,640 Q240,545 395,508"/>
        <path id="arcWeb2" d="M236,650 Q262,590 400,568"/>
      </defs>
      <rect width="405" height="695" fill="#e6e4cc"/>
      <path d="M0,337 Q300,350 405,490 L405,695 L0,695 Z" fill="#d6e29e"/>
      <path d="M0,480 Q220,470 330,695 L0,695 Z" fill="#5f9f3b"/>
      <path d="M0,290 Q180,195 405,197 L405,490 Q300,350 0,337 Z" fill="#80b746"/>
      <path d="M168,695 Q200,520 405,480 L405,695 Z" fill="#e8e6cf"/>
      <path d="M168,695 Q200,520 405,480" fill="none" stroke="var(--purple-ribbon)" stroke-width="11"/>
      <path d="M200,695 Q228,565 405,540" fill="none" stroke="var(--purple-ribbon)" stroke-width="5"/>
      <path d="M228,695 Q255,598 405,585" fill="none" stroke="var(--purple-light)" stroke-width="5"/>
      <path d="M28,0 H106 V150 L67,132 L28,150 Z" fill="var(--purple-ribbon)"/>
      <circle cx="67" cy="82" r="52" fill="var(--white)" stroke="var(--purple-ribbon)" stroke-width="3"/>
      <circle cx="67" cy="82" r="30" fill="var(--badge-green)"/>
      <text class="brand" x="392" y="80" text-anchor="end">Brindle Cove</text>
      <text class="brand" x="392" y="118" text-anchor="end">Pantry</text>
      <text class="organic" x="380" y="183" text-anchor="end">organic</text>
      <text class="product" x="382" y="285" text-anchor="end">Alfalfa</text>
      <text class="sprouts" x="382" y="340" text-anchor="end">SPROUTS</text>
      <text class="french" x="382" y="375" text-anchor="end">Luzerne</text>
      <text class="arc-text"><textPath href="#arcPre2" startOffset="40">PRE-WASHED</textPath></text>
      <text class="arc-text"><textPath href="#arcWeb2" startOffset="8">brindlecovepantry.ca</textPath></text>
      <text class="small" x="15" y="592">KEEP REFRIGERATED</text>
      <text class="small" x="15" y="606">GARDER RÉFRIGÉRATÉ</text>
      <rect x="15" y="613" width="162" height="65" fill="var(--upc-panel)"/>
      <text class="weight" x="305" y="640">100g</text>
      <text class="tiny" x="353" y="631">NET WT</text>
      <text class="tiny" x="353" y="641">POIDS NET</text>
      <text class="postal" x="394" y="661" text-anchor="end">B3K 5X7</text>
      <rect x="257" y="668" width="22" height="13" fill="var(--white)" stroke="#ccc" stroke-width="0.5"/>
      <rect x="257" y="668" width="6" height="13" fill="var(--flag-red)"/>
      <rect x="273" y="668" width="6" height="13" fill="var(--flag-red)"/>
      <rect x="266" y="671" width="4" height="7" fill="var(--flag-red)"/>
      <text class="origin" x="394" y="681" text-anchor="end">Grown in Canada</text>
    </svg>
  </div>

  <!-- Purple ribbon / lime variant -->
  <div class="label label--lime">
    <svg viewBox="0 0 405 695" role="img" aria-label="Brindle Cove Pantry organic alfalfa sprouts label, lime and purple">
      <defs>
        <path id="arcPre3" d="M212,640 Q240,545 395,508"/>
        <path id="arcWeb3" d="M236,650 Q262,590 400,568"/>
      </defs>
      <rect width="405" height="695" fill="#e6e4cc"/>
      <path d="M0,337 Q300,350 405,490 L405,695 L0,695 Z" fill="#a3cb52"/>
      <path d="M0,290 Q180,195 405,197 L405,490 Q300,350 0,337 Z" fill="#5d9e3c"/>
      <path d="M168,695 Q200,520 405,480 L405,695 Z" fill="#e6e2b4"/>
      <path d="M168,695 Q200,520 405,480" fill="none" stroke="var(--purple-ribbon)" stroke-width="11"/>
      <path d="M200,695 Q228,565 405,540" fill="none" stroke="var(--purple-ribbon)" stroke-width="5"/>
      <path d="M228,695 Q255,598 405,585" fill="none" stroke="var(--purple-light)" stroke-width="5"/>
      <path d="M28,0 H106 V150 L67,132 L28,150 Z" fill="var(--purple-ribbon)"/>
      <circle cx="67" cy="82" r="52" fill="var(--white)" stroke="var(--purple-ribbon)" stroke-width="3"/>
      <circle cx="67" cy="82" r="30" fill="var(--badge-green)"/>
      <text class="brand" x="392" y="80" text-anchor="end">Brindle Cove</text>
      <text class="brand" x="392" y="118" text-anchor="end">Pantry</text>
      <text class="organic" x="380" y="183" text-anchor="end">organic</text>
      <text class="product" x="382" y="285" text-anchor="end">Alfalfa</text>
      <text class="sprouts" x="382" y="340" text-anchor="end">SPROUTS</text>
      <text class="french" x="382" y="375" text-anchor="end">Luzerne</text>
      <text class="arc-text"><textPath href="#arcPre3" startOffset="40">PRE-WASHED</textPath></text>
      <text class="arc-text"><textPath href="#arcWeb3" startOffset="8">brindlecovepantry.ca</textPath></text>
      <text class="small" x="15" y="592">KEEP REFRIGERATED</text>
      <text class="small" x="15" y="606">GARDER RÉFRIGÉRATÉ</text>
      <rect x="15" y="613" width="162" height="65" fill="var(--upc-panel)"/>
      <text class="weight" x="305" y="640">100g</text>
      <text class="tiny" x="353" y="631">NET WT</text>
      <text class="tiny" x="353" y="641">POIDS NET</text>
      <text class="postal" x="394" y="661" text-anchor="end">B3K 5X7</text>
      <rect x="257" y="668" width="22" height="13" fill="var(--white)" stroke="#ccc" stroke-width="0.5"/>
      <rect x="257" y="668" width="6" height="13" fill="var(--flag-red)"/>
      <rect x="273" y="668" width="6" height="13" fill="var(--flag-red)"/>
      <rect x="266" y="671" width="4" height="7" fill="var(--flag-red)"/>
      <text class="origin" x="394" y="681" text-anchor="end">Grown in Canada</text>
    </svg>
  </div>

</main>
</body>
</html>
```